Business Card Design Project

Business card design for an IT Service company. A logo has already been created in a different contest and has been attached to this project. Ideally we're looking for a double sided business card that matches the look and feel of our newly created logo.

We're open to creativity if you feel a tag line is needed such as "IT Services and Application Development". We're open to really and look and feel - even single sided business cards if you feel you have something that's a great idea.

Last thought here - I'm not sure how it'll look but maybe a two tone card? One side dark blue and the other side white? Don't limit the design submissions to this tho - just curious if it would look good

Nothing too busy please - simple... Thank you and happy designing!

Target Market(s)

Businesses that require IT Services and support for hosted services, technical consultation, web design.

Industry/Entity Type

Business

Font styles to use
Sans Serif

Requirements
Must have
• Use the colors provided in the logo (see attachment) or additional colors that compliment
Must have the following contact info (not necessarily in this order):
- Alan Fisk
- Founding Partner
- afisk@quillbarrow.example
- 555-382-1946
- www.quillbarrow.example

```html
<!DOCTYPE html>
<html lang="en">
<head>
<meta charset="utf-8">
<title>Quillbarrow Business Card</title>
<link href="https://fonts.googleapis.com/css2?family=Arimo:wght@400;700&display=swap" rel="stylesheet">
<style>
  :root {
    --navy: #1b3461;
    --navy-light: #2a4a78;
    --green: #6f9a48;
    --white: #ffffff;
    --backdrop: #e9e4de;
    --shadow: rgba(40, 30, 20, 0.25);
  }
  html, body {
    margin: 0;
    padding: 0;
    width: 1200px;
    height: 914px;
    overflow: hidden;
    background: var(--backdrop);
    font-family: "Arimo", Arial, sans-serif;
  }
  .canvas {
    position: relative;
    width: 1200px;
    height: 914px;
  }
  .card {
    position: absolute;
    left: 250px;
    width: 700px;
    height: 400px;
    background: var(--white);
    overflow: hidden;
    box-shadow: 0 6px 18px var(--shadow);
  }
  .card--front { top: 40px; }
  .card--back { top: 474px; }
  .card__bands {
    position: absolute;
    inset: 0;
    width: 700px;
    height: 400px;
  }
  .holder {
    position: absolute;
    left: 40px;
    top: 28px;
    color: var(--white);
  }
  .holder__name {
    font-size: 36px;
    font-weight: 400;
    margin: 0;
    letter-spacing: 0.3px;
  }
  .holder__title {
    font-size: 15px;
    margin: 4px 0 0 2px;
  }
  .contacts {
    position: absolute;
    left: 40px;
    top: 112px;
    list-style: none;
    margin: 0;
    padding: 0;
    color: var(--white);
    font-size: 16px;
  }
  .contacts__item {
    display: flex;
    align-items: center;
    height: 30px;
  }
  .contacts__icon {
    width: 16px;
    height: 16px;
    margin-right: 16px;
    flex: none;
  }
  .brand {
    position: absolute;
    right: 44px;
    color: var(--navy);
    font-weight: 700;
    font-size: 52px;
    letter-spacing: -0.5px;
    margin: 0;
  }
  .card--front .brand { bottom: 48px; }
  .card--back .brand { bottom: 86px; }
  .tagline {
    position: absolute;
    right: 44px;
    bottom: 52px;
    margin: 0;
    color: var(--green);
    font-size: 21px;
  }
</style>
</head>
<body>
<main class="canvas">

  <section class="card card--front" aria-label="Card front">
    <svg class="card__bands" viewBox="0 0 700 400" aria-hidden="true">
      <defs>
        <radialGradient id="navyGlowFront" cx="0.35" cy="0.4" r="0.7">
          <stop offset="0" stop-color="#2a4a78"/>
          <stop offset="1" stop-color="#1b3461"/>
        </radialGradient>
      </defs>
      <polygon points="0,0 700,0 700,12 0,372" fill="url(#navyGlowFront)"/>
      <polygon points="0,372 700,12 700,20 0,392" fill="#6f9a48"/>
    </svg>

    <div class="holder">
      <h1 class="holder__name">Alan Fisk</h1>
      <p class="holder__title">Founding Partner</p>
    </div>

    <ul class="contacts">
      <li class="contacts__item">
        <svg class="contacts__icon" viewBox="0 0 20 20" aria-hidden="true">
          <path d="M5 2 L8 2 L9 6 L7 8 Q9 12 12 13 L14 11 L18 12 L18 15 Q17 18 14 18 Q4 16 2 6 Q2 3 5 2 Z" fill="#ffffff"/>
        </svg>
        <span>555-382-1946</span>
      </li>
      <li class="contacts__item">
        <svg class="contacts__icon" viewBox="0 0 20 20" aria-hidden="true">
          <rect x="1.5" y="4.5" width="17" height="11" fill="none" stroke="#ffffff" stroke-width="1.6"/>
          <polyline points="1.5,4.5 10,11 18.5,4.5" fill="none" stroke="#ffffff" stroke-width="1.6"/>
        </svg>
        <span>afisk@quillbarrow.example</span>
      </li>
      <li class="contacts__item">
        <svg class="contacts__icon" viewBox="0 0 20 20" aria-hidden="true">
          <circle cx="10" cy="10" r="8" fill="none" stroke="#ffffff" stroke-width="1.6"/>
          <ellipse cx="10" cy="10" rx="3.5" ry="8" fill="none" stroke="#ffffff" stroke-width="1.3"/>
          <line x1="2" y1="10" x2="18" y2="10" stroke="#ffffff" stroke-width="1.3"/>
        </svg>
        <span>www.quillbarrow.example</span>
      </li>
    </ul>

    <p class="brand">Quillbarrow</p>
  </section>

  <section class="card card--back" aria-label="Card back">
    <svg class="card__bands" viewBox="0 0 700 400" aria-hidden="true">
      <defs>
        <radialGradient id="navyGlowBack" cx="0.3" cy="0.35" r="0.7">
          <stop offset="0" stop-color="#233f6c"/>
          <stop offset="1" stop-color="#1b3461"/>
        </radialGradient>
      </defs>
      <polygon points="0,0 700,0 700,14 0,318" fill="url(#navyGlowBack)"/>
      <polygon points="0,318 700,14 700,20 0,340" fill="#6f9a48"/>
    </svg>

    <p class="brand">Quillbarrow</p>
    <p class="tagline">IT Services and Application Development</p>
  </section>

</main>
</body>
</html>
```